Postcard design to acquire new clients for my Property Management Company

I'm looking for a postcard design that I can send to prospective clients detailing information about my company and services.
Postcard should be eye catching and contain information from www.brightkeyrentals-example.com. I've provided a few screen shots for the most important information and my logo.
Target Market(s)
Real Estate
Industry/Entity Type
Real Estate
Font styles to use
Sans Serif
Requirements
Must have
- Must be eye catching!! this will be a direct mail piece - I'd like for the card to be read and not tossed in the trash immediately.
Design que from the logo.
A place to write / print the receipts name and address.
our physical address - 2287 Marble Lane, Lubbock, TX 79555.
Should not have
- the contact information on the business card is not accurate - please use info from website.

```html
<!DOCTYPE html>
<html lang="en">
<head>
<meta charset="utf-8">
<title>BrightKey Property Management – Postcard</title>
<link href="https://fonts.googleapis.com/css2?family=Arimo:wght@400;700&display=swap" rel="stylesheet">
<style>
  :root {
    --brand-blue: #1f4e8c;
    --panel-blue: #2a5a97;
    --ink: #1e1e1e;
    --paper: #ffffff;
    --backdrop: #ecedef;
    --rule: #3a3a3a;
  }
  * { box-sizing: border-box; margin: 0; padding: 0; }
  html, body { width: 1200px; height: 1199px; overflow: hidden; }
  body {
    background: var(--backdrop);
    font-family: "Arimo", Arial, sans-serif;
    color: var(--ink);
    position: relative;
  }
  .postcard {
    position: absolute;
    left: 193px;
    width: 814px;
    height: 570px;
    background: var(--paper);
    box-shadow: 0 4px 14px rgba(0,0,0,0.25);
    overflow: hidden;
  }
  .postcard--front { top: 20px; }
  .postcard--back { top: 610px; }

  /* Front */
  .front-art { position: absolute; inset: 0; }
  .brand { position: absolute; left: 306px; top: 30px; color: var(--brand-blue); font-weight: 700; }
  .brand__name { font-size: 38px; letter-spacing: 6px; line-height: 1; }
  .brand__tag { font-size: 15px; letter-spacing: 4.2px; margin-top: 4px; }
  .headline {
    position: absolute; left: 306px; top: 124px;
    color: var(--brand-blue); font-weight: 700; font-size: 27px; line-height: 31px;
  }
  .subhead { position: absolute; left: 306px; top: 194px; font-size: 14px; }
  .tier { position: absolute; }
  .tier__name { font-size: 18px; line-height: 20px; }
  .tier__note { font-size: 11.5px; margin-top: 2px; }
  .tier__rate { color: var(--brand-blue); font-weight: 700; font-size: 24px; line-height: 28px; margin-top: 2px; }
  .tier__unit { font-size: 11.5px; }
  .tier__features { position: absolute; font-size: 11.2px; line-height: 15px; }
  .tier--lease { left: 321px; top: 228px; }
  .tier--full { left: 366px; top: 338px; }
  .tier--premium { left: 418px; top: 450px; }
  .tier--lease .tier__features { left: 137px; top: 22px; width: 330px; }
  .tier--full .tier__features { left: 110px; top: 22px; width: 340px; }
  .tier--premium .tier__features { left: 156px; top: 22px; width: 220px; }

  /* Back */
  .services-panel {
    position: absolute; left: 0; top: 0; width: 405px; height: 570px;
    background: var(--panel-blue); color: #fff;
  }
  .services-panel__title { position: absolute; left: 0; width: 405px; top: 28px; text-align: center; font-size: 26px; font-weight: 700; }
  .services-panel__intro { position: absolute; left: 0; width: 405px; top: 62px; text-align: center; font-size: 14px; }
  .service { position: absolute; display: flex; align-items: center; gap: 8px; font-size: 21px; }
  .service svg { width: 37px; height: 37px; flex: none; }
  .contact { position: absolute; left: 0; width: 405px; top: 482px; text-align: center; font-size: 17px; line-height: 26px; }
  .contact strong { font-weight: 700; }
  .stamp-box { position: absolute; left: 676px; top: 37px; width: 98px; height: 98px; border: 1.5px solid var(--rule); }
  .address-line { position: absolute; left: 429px; width: 361px; height: 0; border-top: 1.2px solid var(--rule); }
</style>
</head>
<body>

<section class="postcard postcard--front">
  <svg class="front-art" width="814" height="570" viewBox="0 0 814 570">
    <defs>
      <linearGradient id="photoTone" x1="0" y1="0" x2="1" y2="1">
        <stop offset="0" stop-color="#b9bcb6"/>
        <stop offset="0.5" stop-color="#d9d6d2"/>
        <stop offset="1" stop-color="#9c9590"/>
      </linearGradient>
    </defs>
    <polygon points="0,0 162,0 404,570 0,570" fill="url(#photoTone)" role="img" aria-label="Photo of two hands sheltering a small white model house with a red roof"/>
    <polygon points="162,0 172,0 414,570 404,570" fill="var(--brand-blue)"/>
  </svg>

  <div class="brand">
    <div class="brand__name">BRIGHTKEY</div>
    <div class="brand__tag">PROPERTY MANAGEMENT</div>
  </div>

  <h1 class="headline">CHOOSE THE RIGHT PROPERTY<br>MANAGEMENT SYSTEM</h1>
  <p class="subhead">Selecting the wrong manager could be your costliest mistake ever.</p>

  <div class="tier tier--lease">
    <div class="tier__name">Lease Only</div>
    <div class="tier__note">You Just Need Tenants</div>
    <div class="tier__rate">9%</div>
    <div class="tier__unit">of annual lease</div>
    <div class="tier__features">Professional Photography | Marketing &amp; Advertising<br>Property Showings | Tenant Screening &amp; Qualifications<br>Lease Execution | Move In Coordination</div>
  </div>

  <div class="tier tier--full">
    <div class="tier__name">Full Service</div>
    <div class="tier__note">Our Most Popular</div>
    <div class="tier__rate">10%</div>
    <div class="tier__unit">of monthly rent</div>
    <div class="tier__features">Includes Leasing Service | 24/7 Emergency Response<br>Move In &amp; Out Inspections | Professional Lease Enforcement<br>Schedule &amp; Oversee all Repairs | Pay all Invoices<br>Monthly &amp; Year End Statements | Annual Market Rent Analysis</div>
  </div>

  <div class="tier tier--premium">
    <div class="tier__name">Premium Service</div>
    <div class="tier__note">Our Premier Service</div>
    <div class="tier__rate">12%</div>
    <div class="tier__unit">of monthly rent</div>
    <div class="tier__features">Includes Full Service Features<br>Professional Video Marketing<br>Home Warranty Coordination<br>Tenant Retention Program</div>
  </div>
</section>

<section class="postcard postcard--back">
  <div class="services-panel">
    <h2 class="services-panel__title">Discover Our Services</h2>
    <p class="services-panel__intro">We offer full-service property management solutions</p>

    <div class="service" style="left:32px;top:86px">
      <svg viewBox="0 0 40 40" fill="none" stroke="#fff" stroke-width="2.2"><circle cx="20" cy="20" r="18"/><path d="M10 21 L20 12 L30 21 M13 19 V29 H27 V19" fill="#fff" stroke-linejoin="round"/></svg>
      <span>Property Marketing</span>
    </div>
    <div class="service" style="left:147px;top:136px">
      <svg viewBox="0 0 40 40" fill="none" stroke="#fff" stroke-width="2.2"><circle cx="20" cy="20" r="18"/><circle cx="15" cy="16" r="3.5" fill="#fff"/><circle cx="25" cy="16" r="3.5" fill="#fff"/><path d="M9 28 Q15 20 21 28 Z M19 28 Q25 20 31 28 Z" fill="#fff"/></svg>
      <span>Tenant Screening</span>
    </div>
    <div class="service" style="left:32px;top:186px">
      <svg viewBox="0 0 40 40" fill="none" stroke="#fff" stroke-width="2.2"><circle cx="20" cy="20" r="18"/><path d="M24 14 Q20 11 16.5 13.5 Q14 16.5 19 19 Q25 21 23 25.5 Q20 28.5 15.5 26 M20 9 V31"/></svg>
      <span style="margin-left:10px">Rent Collection</span>
    </div>
    <div class="service" style="left:147px;top:230px">
      <svg viewBox="0 0 40 40" fill="none" stroke="#fff" stroke-width="2.2"><circle cx="20" cy="20" r="18"/><path d="M13 28 L23 17 M19 13 L26 13 L28 17 L24 20 Z" fill="#fff" stroke-linejoin="round"/></svg>
      <span style="margin-left:10px">Maintenance</span>
    </div>
    <div class="service" style="left:32px;top:275px">
      <svg viewBox="0 0 40 40" fill="none" stroke="#fff" stroke-width="2.2"><circle cx="20" cy="20" r="18"/><circle cx="18" cy="18" r="6"/><path d="M22.5 22.5 L28 28" stroke-width="3"/></svg>
      <span style="margin-left:10px">Property Inspections</span>
    </div>
    <div class="service" style="left:147px;top:324px">
      <svg viewBox="0 0 40 40" fill="none" stroke="#fff" stroke-width="2.2"><circle cx="20" cy="20" r="18"/><path d="M12 12 V28 H28 M16 25 V19 M20 25 V16 M24 25 V20" /></svg>
      <span style="margin-left:10px">Financial Reporting</span>
    </div>
    <div class="service" style="left:32px;top:373px">
      <svg viewBox="0 0 40 40" fill="none" stroke="#fff" stroke-width="2.2"><circle cx="20" cy="20" r="18"/><path d="M20 10 L28 13 V20 Q28 27 20 31 Q12 27 12 20 V13 Z M20 13 V28"/></svg>
      <span style="margin-left:10px">Evictions</span>
    </div>
    <div class="service" style="left:147px;top:419px">
      <svg viewBox="0 0 40 40" fill="none" stroke="#fff" stroke-width="2.2"><circle cx="20" cy="20" r="18"/><path d="M20 11 V28 M14 28 H26 M12 15 H28 M12 15 L9 22 H15 Z M28 15 L25 22 H31 Z"/></svg>
      <span style="margin-left:10px">Legal Guidance</span>
    </div>

    <div class="contact">
      2287 Marble Lane, Lubbock, TX 79555<br>
      <strong>(806) 555-0142</strong> | info@brightkeyrentals-example.com<br>
      www.brightkeyrentals-example.com
    </div>
  </div>

  <div class="stamp-box" aria-label="Stamp area"></div>
  <div class="address-line" style="top:300px"></div>
  <div class="address-line" style="top:362px"></div>
  <div class="address-line" style="top:423px"></div>
  <div class="address-line" style="top:485px"></div>
</section>

</body>
</html>
```